Design some Business Cards

I used Taskvoro to have our logo designed - our Taskvoro did a great job and we are so pleased. BLACK BUSINESS CARDS

Repairs Rebuilds Renovations Can we get this somewhere on the card by the logo on the one side of the card?

Circled logo on back or card - centered

Logo and company name on other side.

Dorin Velasko
217 Larkspur Ridge Close
Chestermere, AB
R4G 2W7

(403) 555-0172 Phone
(403) 555-0184 Fax
rbvelasko@pelmora.ca

We are looking for something fun and memorable.

Specializing in:

Retail Store Maintenance and Construction
Residential and Commercial Painting
Flooring

Horizontal placement please

```html
<!DOCTYPE html>
<html lang="en">
<head>
<meta charset="utf-8">
<title>Velasko Painting and Repairs – Business Cards</title>
<link rel="stylesheet" href="https://fonts.googleapis.com/css2?family=Questrial&display=swap">
<style>
  :root {
    --page: #e6e6e7;
    --card: #070708;
    --card-sheen: #1a1b1e;
    --blue: #4aa6ec;
    --blue-deep: #2b6fc4;
    --text: #b9bcc2;
    --text-dim: #8c9097;
  }
  * { margin: 0; padding: 0; box-sizing: border-box; }
  html, body { width: 1200px; height: 740px; overflow: hidden; }
  body {
    background: var(--page);
    font-family: "Questrial", "Century Gothic", sans-serif;
    position: relative;
  }
  .card {
    position: absolute;
    top: 222px;
    width: 500px;
    height: 290px;
    border-radius: 3px;
    background: linear-gradient(135deg, var(--card-sheen) 0%, var(--card) 45%, var(--card) 100%);
    box-shadow: 0 10px 24px rgba(0,0,0,0.22);
    overflow: hidden;
    color: var(--text);
  }
  .card--front { left: 70px; }
  .card--back { left: 630px; }

  /* front */
  .services {
    position: absolute;
    left: 26px;
    top: 42px;
    width: 240px;
    list-style: none;
    font-size: 12px;
    line-height: 22px;
    color: var(--text);
    white-space: nowrap;
  }
  .brand {
    position: absolute;
    right: 24px;
    top: 36px;
    width: 180px;
    display: flex;
    align-items: center;
    gap: 10px;
  }
  .brand__mark {
    width: 40px; height: 40px;
    border-radius: 50%;
    border: 3px solid var(--blue);
    flex: none;
  }
  .brand__name {
    font-size: 18px;
    line-height: 22px;
    color: var(--blue);
    width: 130px;
  }
  .divider {
    position: absolute;
    left: 0; right: 0;
    top: 168px;
    height: 3px;
    background: linear-gradient(90deg, var(--blue-deep), var(--blue) 60%, rgba(74,166,236,0.2));
  }
  .contacts {
    position: absolute;
    left: 26px;
    top: 186px;
    list-style: none;
    font-size: 11.5px;
    line-height: 18px;
    color: var(--text-dim);
  }
  .contacts li { display: flex; align-items: center; gap: 8px; white-space: nowrap; }
  .contacts svg { width: 11px; height: 11px; flex: none; }
  .contacts .address-line { padding-left: 19px; }
  .person {
    position: absolute;
    right: 26px;
    top: 196px;
    font-size: 24px;
    color: var(--text-dim);
    letter-spacing: 0.5px;
    white-space: nowrap;
  }

  /* back */
  .taglines {
    position: absolute;
    left: 30px;
    top: 34px;
    list-style: none;
    font-size: 14px;
    color: var(--blue);
  }
  .taglines li { margin-bottom: 28px; }
  .taglines li:nth-child(2) { padding-left: 22px; }
  .taglines li:nth-child(3) { padding-left: 44px; }
  .emblem {
    position: absolute;
    right: 70px;
    top: 50%;
    transform: translateY(-50%);
    display: flex;
    align-items: center;
    gap: 14px;
  }
  .emblem__ring {
    width: 110px; height: 110px;
    border-radius: 50%;
    border: 4px solid var(--blue);
    flex: none;
  }
  .emblem__name {
    font-size: 26px;
    color: var(--blue);
  }
</style>
</head>
<body>

<section class="card card--front" aria-label="Business card front">
  <ul class="services">
    <li>Retail Store Maintenance and Construction</li>
    <li>Residential and Commercial Painting</li>
    <li>Colour Consult and Design</li>
    <li>Flooring</li>
  </ul>

  <div class="brand">
    <span class="brand__mark"></span>
    <span class="brand__name">Velasko Painting and Repairs</span>
  </div>

  <div class="divider"></div>

  <ul class="contacts">
    <li>
      <svg viewBox="0 0 12 12" fill="none" stroke="#8c9097" stroke-width="1.2"><path d="M2.5 1.5h2l1 2.5-1.3 1a6 6 0 0 0 2.8 2.8l1-1.3 2.5 1v2a1 1 0 0 1-1 1A9 9 0 0 1 1.5 2.5a1 1 0 0 1 1-1z"/></svg>
      (403) 555-0172
    </li>
    <li>
      <svg viewBox="0 0 12 12" fill="none" stroke="#8c9097" stroke-width="1.2"><rect x="3" y="1.5" width="6" height="3"/><rect x="1.5" y="4.5" width="9" height="4"/><rect x="3" y="7.5" width="6" height="3"/></svg>
      (403) 555-0184
    </li>
    <li>
      <svg viewBox="0 0 12 12" fill="none" stroke="#8c9097" stroke-width="1.2"><rect x="1" y="2.5" width="10" height="7"/><path d="M1 2.5l5 4 5-4"/></svg>
      rbvelasko@pelmora.ca
    </li>
    <li>
      <svg viewBox="0 0 12 12" fill="none" stroke="#8c9097" stroke-width="1.2"><path d="M6 11s3.5-3.6 3.5-6.3a3.5 3.5 0 0 0-7 0C2.5 7.4 6 11 6 11z"/><circle cx="6" cy="4.7" r="1.2"/></svg>
      217 Larkspur Ridge Close
    </li>
    <li class="address-line">Chestermere, AB &nbsp;R4G 2W7</li>
  </ul>

  <div class="person">Dorin Velasko</div>
</section>

<section class="card card--back" aria-label="Business card back">
  <ul class="taglines">
    <li>Repairs</li>
    <li>Rebuilds</li>
    <li>Renovations</li>
  </ul>

  <div class="emblem">
    <span class="emblem__ring"></span>
    <span class="emblem__name">Velasko</span>
  </div>
</section>

</body>
</html>
```